Webdesign für ambulanter Pflegedienst
Zielgruppe
Es ist ein ambulanter Pflegedienst, der sich im Raum Dessau-Roßlau um die Versorgung sowie Betreuung von Menschen kümmert. Kontaktdaten: ambulanter Pflegedienst Lindra Pflege; Inhaberin: Marta Waldhuber; Birkenhagweg 14, 06795 Dessau-Roßlau Telefon: 034907/519463
IK-Nummer: 38 604 7193
e-mail: mw-lindra-pflege@postfach-beispiel.de
Aufgabenstellung
Die Farben sollen in Anlehnung an das Logo sein, dass mit übersandt wird.

```html
<!DOCTYPE html>
<html lang="de">
<head>
<meta charset="utf-8">
<title>Karriere – Lindra Pflege</title>
<link href="https://fonts.googleapis.com/css2?family=Raleway:wght@400;500;600;700&family=Indie+Flower&display=swap" rel="stylesheet">
<style>
:root{
  --teal:#4aaea8;
  --teal-light:#b6ddd9;
  --green:#8cba4e;
  --text:#5f5f5f;
  --heading:#555555;
  --sky:#dcedf8;
  --border:#e3e3e3;
  --white:#ffffff;
}
*{box-sizing:border-box;margin:0;padding:0}
html,body{width:1200px;height:4199px;overflow:hidden}
body{position:relative;background:var(--white);font-family:'Raleway',sans-serif;color:var(--text);font-size:12px;line-height:16px}
.abs{position:absolute}
.script{font-family:'Indie Flower',cursive;color:var(--heading)}
.center{text-align:center}
.h2{font-size:30px;line-height:34px;font-weight:600;color:var(--heading)}
.h2 .accent{color:var(--teal)}
.rule{position:absolute;left:572px;width:56px;height:3px;background:var(--green)}
.lead{left:340px;width:520px;text-align:center}
/* navigation */
.nav-link{top:18px;font-size:13px;color:var(--text)}
.nav-link.active{color:var(--green);font-weight:700}
.brand{font-weight:700;color:var(--teal);font-size:13px}
/* cards */
.card{position:absolute;background:var(--white);border:1px solid var(--border);box-shadow:0 2px 8px rgba(0,0,0,.12);border-radius:3px;text-align:center;padding:0 34px}
.card h3{font-family:'Indie Flower',cursive;font-weight:400;font-size:17px;color:var(--heading);margin:60px 0 14px}
.card p{font-size:12px;line-height:18px}
.icon-bubble{position:absolute;width:84px;height:84px;border-radius:50%;background:linear-gradient(180deg,#f2f6f3,#b9ddd8);display:flex;align-items:center;justify-content:center}
/* checklist */
.panel{position:absolute;background:var(--white);box-shadow:0 2px 10px rgba(0,0,0,.14);border-radius:3px;overflow:hidden}
.panel-head{height:54px;background:var(--sky);font-family:'Indie Flower',cursive;font-size:17px;color:var(--heading);line-height:54px}
.check-item{position:absolute;width:260px}
.check-item h4{font-size:15px;font-weight:700;color:var(--heading);margin:0 0 14px 34px;line-height:20px}
.check-item p{margin-left:34px;font-size:12px;line-height:16px}
.check-item svg{position:absolute;left:0;top:-6px}
/* form */
.label{font-size:12px;color:var(--heading)}
.field{position:absolute;border:1px solid #cfcfcf;border-radius:4px;background:var(--white)}
.drop{position:absolute;border:1px solid var(--teal);background:#e9f5f3;border-radius:2px;text-align:center;font-size:9px;color:var(--text)}
.file{font-size:10px;color:var(--green);text-decoration:underline}
.btn{position:absolute;background:var(--teal);color:var(--white);font-weight:700;font-size:12px;border-radius:22px;text-align:center;line-height:42px}
/* team */
.person{position:absolute;width:190px;text-align:center}
.portrait{width:150px;height:150px;border-radius:50%;margin:0 auto 20px;background:radial-gradient(circle at 50% 45%,#e2c8a8 0,#c29a6e 40%,#6f5232 100%)}
.person .name{font-size:13px;color:var(--heading);line-height:16px}
.person .role{font-size:10px;color:var(--text);line-height:14px}
/* footer */
.foot-link{top:4169px;font-size:10px;font-weight:700;color:var(--heading)}
</style>
</head>
<body>

<!-- header -->
<header>
  <div class="abs" style="left:266px;top:20px;display:flex;align-items:center;gap:6px">
    <span style="display:inline-block;width:14px;height:14px;border-radius:50%;background:var(--teal)"></span>
    <span class="brand">Lindra Pflege</span>
  </div>
  <nav>
    <span class="abs nav-link" style="left:418px">Startseite</span>
    <span class="abs nav-link" style="left:505px">Sofortige Hilfen</span>
    <span class="abs nav-link" style="left:623px">Unsere Leistungen</span>
    <span class="abs nav-link active" style="left:760px">Karriere</span>
    <span class="abs nav-link" style="left:833px">Pflegekurse</span>
  </nav>
</header>

<div class="abs center" style="left:0;top:52px;width:1200px;height:24px;background:var(--sky);font-size:10px;line-height:24px;color:var(--teal)">
  Lindra Pflege – <span class="script" style="font-size:11px">Pflege von Mensch zu Mensch</span>
</div>

<!-- hero -->
<section>
  <div class="abs" style="left:0;top:76px;width:1200px;height:180px;background:linear-gradient(90deg,var(--teal-light) 0%,#d7ebe7 35%,#f0f2ee 55%,#f0f2ee 100%)"></div>
  <div class="abs" role="img" aria-label="Foto: medizinische Mund-Nasen-Schutzmasken" style="left:660px;top:76px;width:540px;height:180px;background:linear-gradient(100deg,rgba(240,242,238,0) 0%,#d7e9f1 25%,#c4e0ec 55%,#e4f0f5 80%,#cde3ee 100%)"></div>
  <div class="abs script" style="left:263px;top:128px;font-size:17px">Wir suchen Dich!</div>
  <h1 class="abs" style="left:262px;top:153px;font-size:33px;line-height:40px;font-weight:600;color:var(--heading)">Karriere bei uns</h1>
  <div class="abs" style="left:715px;top:163px;width:144px;height:144px;border-radius:50%;background:var(--white);box-shadow:0 2px 10px rgba(0,0,0,.15);display:flex;align-items:center;justify-content:center">
    <svg width="76" height="60" viewBox="0 0 76 60" fill="none" stroke="#555" stroke-width="2.5" stroke-linejoin="round">
      <rect x="3" y="13" width="70" height="44" rx="4"/>
      <path d="M27 13V6a3 3 0 0 1 3-3h16a3 3 0 0 1 3 3v7"/>
      <path d="M3 34h30M43 34h30"/>
      <rect x="33" y="29" width="10" height="11" rx="1"/>
    </svg>
  </div>
</section>

<!-- intro -->
<section>
  <div class="abs script center" style="left:0;top:360px;width:1200px;font-size:15px">Pflege mit Herz &amp; Seele</div>
  <h2 class="abs h2 center" style="left:0;top:392px;width:1200px">Komm in unser <span class="accent">Lindra Pflege</span></h2>
  <div class="rule" style="top:444px"></div>
  <p class="abs lead" style="top:474px">Gehörst du zu den Menschen, die mit Herz und Seele Anderen zur Seite steht, unterstützt und versorgt, dann bist du hier genau richtig. Hilf uns die Pflege in der Umgebung Dessau-Roßlau qualitativ zu verbessern und menschlicher zu gestalten.</p>
  <p class="abs lead" style="top:538px">Wir wissen, dass zufriedene Mitarbeiter bessere Arbeit leisten. Dies kommt nicht nur unseren Patienten zugute, sondern auch dem Teamgeist. Daher möchten wir ein Paar Goodies auflisten, die Mitarbeiter bei uns erhalten.</p>
</section>

<!-- benefits -->
<section>
  <div class="card" style="left:285px;top:676px;width:303px;height:305px">
    <h3>Urlaub</h3>
    <p>Bei uns erhält jeder Mitarbeiter 30 Tage Urlaub. Da wir wissen, wie wichtig Erholung ist. Weiterhin nehmen wir Rücksicht auf die individuelle Situation eines Mitarbeiters und versuchen die Dienstplan- und Tourengestaltung demnach anzupassen.</p>
  </div>
  <div class="icon-bubble" style="left:395px;top:628px">
    <svg width="38" height="30" viewBox="0 0 38 30" fill="none" stroke="#555" stroke-width="1.5"><path d="M4 12a12 9 0 0 1 24 0z"/><path d="M16 12v12M2 26h34"/><path d="M20 20c3-1 6-1 9 0"/><path d="M30 4l2-1M33 6l2-1"/></svg>
  </div>

  <div class="card" style="left:608px;top:676px;width:303px;height:188px">
    <h3>Sonderleistungen</h3>
    <p>Weitere Sonderleistungen sind möglich. Sprich einfach mit uns und wir werden eine geeignete Lösung zusammen finden.</p>
  </div>
  <div class="icon-bubble" style="left:718px;top:628px">
    <svg width="28" height="32" viewBox="0 0 28 32" fill="none" stroke="#555" stroke-width="1.5"><path d="M3 2h18v16M3 2v28h14"/><path d="M7 9h10M7 14h10M7 19h6"/><path d="M22 22v8M18 26h8"/></svg>
  </div>

  <div class="card" style="left:608px;top:929px;width:303px;height:305px">
    <h3>Fort- &amp; Weiterbildungen</h3>
    <p>Finden interne und externe Fort- und Weiterbildungen statt, die bei voller Kostenübernahme, nach den individuellen Wünschen der Mitarbeiter ausgerichtet wird. Wir bilden dich gern zur Fachkraft aus. Egal welche Weiterbildung du machen möchtest wir stehen dir bei und werden dafür Sorge tragen, dass sie positiv beendet wird.</p>
  </div>
  <div class="icon-bubble" style="left:718px;top:880px">
    <svg width="34" height="26" viewBox="0 0 34 26" fill="none" stroke="#555" stroke-width="1.5"><path d="M17 5C13 2 7 2 2 3v19c5-1 11-1 15 2 4-3 10-3 15-2V3c-5-1-11-1-15 2z"/><path d="M17 5v19M6 8h7M6 12h7M21 8h7M21 12h7"/></svg>
  </div>

  <div class="card" style="left:285px;top:1046px;width:303px;height:188px">
    <h3>Überdurchschnittliche Vergütung</h3>
    <p>Bei uns erhaltet ihr einen Zuschlag an Sonn- und Feiertagen von 100%.</p>
  </div>
  <div class="icon-bubble" style="left:395px;top:998px">
    <svg width="28" height="28" viewBox="0 0 28 28" fill="none" stroke="#555" stroke-width="1.5"><rect x="3" y="8" width="22" height="17" rx="3"/><path d="M7 8l8-5 4 5"/><rect x="17" y="13" width="8" height="6" rx="1"/></svg>
  </div>
</section>

<!-- expectations -->
<section>
  <div class="abs script center" style="left:0;top:1297px;width:1200px;font-size:15px">Wir zählen auf Dich</div>
  <h2 class="abs h2 center" style="left:0;top:1322px;width:1200px">Was wird auf Dich<br>zukommen?</h2>
  <div class="rule" style="top:1412px"></div>
  <p class="abs lead" style="top:1436px">Die ambulante Pflege wird in der Häuslichkeit der Patienten durchgeführt. Es ist unser Ziel die Pflege für alle Beteiligten so würdevoll und respektvoll zu gestalten wie möglich. Der zu betreuende Mensch steht dabei im Vordergrund, daher gewähren wir jedem die Zeit, die er braucht. Eine funktionierende Zusammenarbeit unter den Mitarbeitern ist uns genauso wichtig. Daher haben wir immer ein offenes Ohr für Patienten, Mitarbeiter und Angehöriger gleichermaßen.</p>

  <div class="panel" style="left:262px;top:1594px;width:674px;height:535px">
    <div class="panel-head" style="padding-left:30px">Deine Checkliste, das bringst Du mit</div>
  </div>

  <div class="check-item" style="left:302px;top:1678px">
    <svg width="26" height="24" viewBox="0 0 26 24"><rect x="1" y="3" width="20" height="20" fill="none" stroke="#cfe6e3" stroke-width="1.5"/><path d="M5 12l6 6L24 2" fill="none" stroke="var(--teal)" stroke-width="4" stroke-linecap="round"/></svg>
    <h4>Teamfähigkeit</h4>
    <p>Unser Hauptaugenmerk liegt auf der Teamfähigkeit. Dies bedeutet nicht nur unter den Mitarbeitern, sondern gegenüber den Angehörigen, den Patienten sowie anderen Professionen. Dabei ist uns ein harmonisches Miteinander sehr wichtig.</p>
  </div>
  <div class="check-item" style="left:302px;top:1832px">
    <svg width="26" height="24" viewBox="0 0 26 24"><rect x="1" y="3" width="20" height="20" fill="none" stroke="#cfe6e3" stroke-width="1.5"/><path d="M5 12l6 6L24 2" fill="none" stroke="var(--teal)" stroke-width="4" stroke-linecap="round"/></svg>
    <h4>Hilfsbereitschaft</h4>
    <p>Sind zur Teamfähigkeit ist die Hilfsbereitschaft sehr wichtig. Wir unterstützen uns alle gegenseitig und Sorgen auf diese Weise für ein gutes Betriebsklima.</p>
  </div>
  <div class="check-item" style="left:302px;top:1984px">
    <svg width="26" height="24" viewBox="0 0 26 24"><rect x="1" y="3" width="20" height="20" fill="none" stroke="#cfe6e3" stroke-width="1.5"/><path d="M5 12l6 6L24 2" fill="none" stroke="var(--teal)" stroke-width="4" stroke-linecap="round"/></svg>
    <h4>Gute Deutschkenntnisse</h4>
    <p>…in Wort und Schrift sind erforderlich, um sich mit den Patienten unterhalten zu können und der Dokumentationspflicht in Schriftform nachzukommen.</p>
  </div>
  <div class="check-item" style="left:611px;top:1678px">
    <svg width="26" height="24" viewBox="0 0 26 24"><rect x="1" y="3" width="20" height="20" fill="none" stroke="#cfe6e3" stroke-width="1.5"/><path d="M5 12l6 6L24 2" fill="none" stroke="var(--teal)" stroke-width="4" stroke-linecap="round"/></svg>
    <h4>Engagement</h4>
    <p>Egal ob du Quereinsteiger bist oder bereits Erfahrung im Pflegeberuf sammeln konntest, wenn du bereit bist deinen Wissensschatz stetig zu erweitern, bist du bei uns genau richtig. Wir sind der Meinung, dass niemand alles wissen kann, wenn jedoch die Bereitschaft zum Lernen besteht, ist das die halbe Miete. Wichtig ist, dass die Einstellung stimmt, den Rest bringen wir dir bei.</p>
  </div>
  <div class="check-item" style="left:611px;top:1906px">
    <svg width="26" height="24" viewBox="0 0 26 24"><rect x="1" y="3" width="20" height="20" fill="none" stroke="#cfe6e3" stroke-width="1.5"/><path d="M5 12l6 6L24 2" fill="none" stroke="var(--teal)" stroke-width="4" stroke-linecap="round"/></svg>
    <h4>Führerschein der Klasse B</h4>
    <p>Du bekommst von uns ein Auto gestellt, damit du zu den Patienten fahren kannst. Sollte keinen Führerschein vorhanden sein, stellen wir ein E-bike zur Verfügung und achten bei der Tourenplangestaltung auf die Distanz zum Patienten.</p>
  </div>
</section>

<!-- questions & form -->
<section>
  <h2 class="abs h2 center" style="left:0;top:2202px;width:1200px">Noch Fragen?</h2>
  <div class="rule" style="top:2253px"></div>
  <p class="abs center" style="left:400px;top:2277px;width:400px">Dann sprich mit uns und wir werden diese bei einem gemeinsamen Treffen zusammen klären. Du kannst dich über folgendes Formular direkt bei uns bewerben. Wir melden uns auf jeden Fall bei dir.</p>

  <div class="panel" style="left:331px;top:2404px;width:525px;height:775px">
    <div class="panel-head center">Bewirb Dich direkt online!</div>
  </div>

  <span class="abs label" style="left:370px;top:2492px">Nachname<sup>*</sup></span>
  <span class="abs label" style="left:608px;top:2492px">Vorname<sup>*</sup></span>
  <div class="field" style="left:370px;top:2515px;width:223px;height:40px"></div>
  <div class="field" style="left:608px;top:2515px;width:222px;height:40px"></div>

  <span class="abs label" style="left:370px;top:2568px">E-Mail<sup>*</sup></span>
  <span class="abs label" style="left:641px;top:2568px">Telefonnummer<sup>*</sup></span>
  <div class="field" style="left:370px;top:2592px;width:256px;height:38px"></div>
  <div class="field" style="left:641px;top:2592px;width:189px;height:38px"></div>

  <span class="abs label" style="left:370px;top:2645px">Möchtest Du noch etwas zu Deiner Bewerbung sagen?</span>
  <div class="field" style="left:370px;top:2667px;width:460px;height:84px"></div>

  <span class="abs label" style="left:370px;top:2766px">Anlagen beifügen</span>
  <p class="abs" style="left:370px;top:2792px;width:460px;font-size:9px;line-height:14px">Ziehe per Drag &amp; Drop deine Bewerbungsunterlagen in das Fenster oder klicke auf „Computer durchsuchen“. Wir wünschen uns von Dir ein Anschreiben, Lebenslauf, (xxxx).</p>
  <div class="drop" style="left:370px;top:2836px;width:460px;height:106px;padding-top:36px;line-height:16px">
    Datei hier hinziehen<br><span style="font-size:7px">oder</span><br><span style="color:var(--teal);text-decoration:underline">Computer durchsuchen</span>
  </div>

  <span class="abs label" style="left:370px;top:2958px">Deine Anlagen</span>
  <span class="abs file" style="left:370px;top:2982px">Lebenslauf_062023_erika-beispiel.pdf</span>
  <span class="abs file" style="left:370px;top:3003px">Anschreiben_062023_erika-beispiel.pdf</span>
  <svg class="abs" style="left:582px;top:2983px" width="10" height="12" viewBox="0 0 10 12" fill="#999"><rect x="1" y="3" width="8" height="9" rx="1"/><rect x="0" y="1" width="10" height="1.5"/><rect x="3" y="0" width="4" height="1.5"/></svg>
  <svg class="abs" style="left:588px;top:3004px" width="10" height="12" viewBox="0 0 10 12" fill="#999"><rect x="1" y="3" width="8" height="9" rx="1"/><rect x="0" y="1" width="10" height="1.5"/><rect x="3" y="0" width="4" height="1.5"/></svg>

  <div class="field" style="left:370px;top:3053px;width:28px;height:26px"></div>
  <p class="abs" style="left:411px;top:3052px;width:420px;font-size:9px;line-height:13px">Du erklärst Dich damit einverstanden, dass Deine Daten zur Bearbeitung Deiner Bewerbung verwendet werden. Weitere Informationen und Widerrufshinweise findest Du in der <span style="color:var(--teal)">Datenschutzerklärung</span>.</p>

  <div class="btn" style="left:673px;top:3117px;width:152px;height:42px">Abenden</div>
</section>

<!-- team -->
<section>
  <div class="abs script center" style="left:0;top:3258px;width:1200px;font-size:15px">Wir freuen uns auf Dich!</div>
  <h2 class="abs h2 center" style="left:0;top:3284px;width:1200px">Das sind deine Kolleg*innen<br>im<span class="accent">Lindra Pflege</span></h2>
  <div class="rule" style="top:3370px"></div>

  <div class="person" style="left:313px;top:3430px"><div class="portrait" role="img" aria-label="Porträtfoto einer Mitarbeiterin"></div><div class="name">Lena Hofbauer</div><div class="role">Berufsbezeichnung</div></div>
  <div class="person" style="left:503px;top:3430px"><div class="portrait" role="img" aria-label="Porträtfoto einer Mitarbeiterin"></div><div class="name">Lena Hofbauer</div><div class="role">Berufsbezeichnung</div></div>
  <div class="person" style="left:694px;top:3430px"><div class="portrait" role="img" aria-label="Porträtfoto einer Mitarbeiterin"></div><div class="name">Lena Hofbauer</div><div class="role">Berufsbezeichnung</div></div>
  <div class="person" style="left:409px;top:3656px"><div class="portrait" role="img" aria-label="Porträtfoto einer Mitarbeiterin"></div><div class="name">Lena Hofbauer</div><div class="role">Berufsbezeichnung</div></div>
  <div class="person" style="left:599px;top:3656px"><div class="portrait" role="img" aria-label="Porträtfoto einer Mitarbeiterin"></div><div class="name">Lena Hofbauer</div><div class="role">Berufsbezeichnung</div></div>
</section>

<!-- footer -->
<footer>
  <div class="abs" style="left:0;top:3915px;width:1200px;height:235px;background:linear-gradient(90deg,var(--teal-light) 0%,#cfe6e2 30%,#eef2ee 50%,#eef2ee 58%,rgba(238,242,238,0) 70%)"></div>
  <div class="abs" role="img" aria-label="Foto: viele Hände übereinander als Zeichen des Zusammenhalts" style="left:700px;top:3915px;width:500px;height:235px;background:linear-gradient(100deg,#eadbc9 0%,#d8b08a 30%,#b98458 60%,#9c6a45 100%)"></div>
  <div class="abs" style="left:0;top:3915px;width:1200px;height:235px;background:linear-gradient(90deg,rgba(0,0,0,0) 0%,rgba(0,0,0,0) 55%,rgba(238,242,238,1) 58%,rgba(238,242,238,0) 68%)"></div>

  <div class="abs script" style="left:262px;top:3946px;font-size:21px">Wir sind für Sie da!</div>
  <p class="abs" style="left:262px;top:3988px;font-size:12px;line-height:19px">ambulanter Pflegedienst Lindra Pflege<br>Inhaberin: Marta Waldhuber<br>Birkenhagweg 14<br>06795 Dessau-Roßlau</p>
  <p class="abs" style="left:262px;top:4074px;font-size:12px;line-height:19px">034907/519463<br>mw-lindra-pflege@postfach-beispiel.de</p>

  <div class="abs center" style="left:500px;top:4010px;width:200px">
    <span style="display:block;width:40px;height:40px;margin:0 auto 12px;border-radius:50%;background:var(--teal)"></span>
    <span style="font-size:17px;font-weight:700;color:var(--heading)">Lindra Pflege</span>
  </div>

  <div class="abs center" style="left:833px;top:3876px;width:104px;height:104px;border-radius:50%;background:var(--sky)">
    <svg style="margin-top:26px" width="18" height="28" viewBox="0 0 18 28"><path d="M9 2v25" stroke="var(--green)" stroke-width="3"/><path d="M1 12L9 2l8 10z" fill="var(--green)"/></svg>
    <div class="script" style="font-size:14px;line-height:16px">Nach oben</div>
  </div>

  <div class="abs" style="left:0;top:4150px;width:1200px;height:49px;background:var(--sky)"></div>
  <span class="abs foot-link" style="left:276px">KARRIERE</span>
  <span class="abs foot-link" style="left:371px">KONTAKT</span>
  <span class="abs foot-link" style="left:471px">DATENSCHUTZ</span>
  <span class="abs foot-link" style="left:597px">IMPRESSUM</span>
  <span class="abs" style="left:707px;top:4169px;font-size:9px;color:var(--text)">Copyright 2023 © ambulanter Pflegedienst Lindra Pflege</span>
</footer>

</body>
</html>
```